Etiketten-Design für Weinflaschen gesucht
Zielgruppe
Wir sind ein Weingut und suchen für unsere Weinflaschen ein neues Etikettdesign.
Aufgabenstellung
Im Anhang sieht man unsere leeren Weinflaschen mit den neuen Kapseln. Dazu passend suchen wir die Etiketten.
Grundfarbe des Etikettes ist Weiß, Größe ca. 11cm hoch & 9cm breit!
Jede Sorte hat ihrer eigene Farbe - diese ist am Kapsel sichtbar und soll sich auch leicht im Etikett
wieder finden.
Etiketten vom Grunddesign gleich + jedoch nur an STELLEN ANDERS EINGEFÄRBT.
Am Etikett zu finden sollte sein:
- Unser Logo mit Namen (Weingut muss nicht vorhanden sein am Etikett)
- Kirchenlogo
- Sorte von Wein:
(Grüner Veltliner - Grün
Traminer - Blau
Rheinriesling - Orange
Blaufränkisch - Rot
St.Lauerent -Gelb
Zweigelt - Weiß)

```html
<!DOCTYPE html>
<html lang="de">
<head>
<meta charset="utf-8">
<title>Hallberger Weingut – Etikettenserie</title>
<link rel="stylesheet" href="https://fonts.googleapis.com/css2?family=Cormorant+Garamond:wght@500&family=Montserrat:wght@400;500&display=swap">
<style>
  :root{
    --ink:#1f1f1f;
    --muted:#7a7a7a;
    --paper:#f7f7f6;
    --ring:#d4d4d4;
    --green:#9cc63f;  --green-tint:#c9cdbb;
    --blue:#3a62b3;   --blue-tint:#b5b7d8;
    --orange:#dc6232; --orange-tint:#e4b6a6;
    --red:#d83a2e;    --red-tint:#e2b5ae;
    --yellow:#d9b730; --yellow-tint:#d8cfaa;
    --grey:#b3b3b3;   --grey-tint:#d8d8d8;
  }
  *{box-sizing:border-box;margin:0;padding:0}
  html,body{width:774px;height:1200px;overflow:hidden;background:#fff}
  .sheet{position:relative;width:774px;height:1200px}

  .label{
    position:absolute;
    width:21.2em;height:26em;
    overflow:hidden;
    background:radial-gradient(ellipse 70% 65% at 50% 50%, var(--paper) 35%, var(--tint) 100%);
    font-family:"Montserrat",sans-serif;
  }
  .label.tall{height:27.5em}
  .label .stripe{position:absolute;left:0;right:0;height:.45em;background:var(--c)}
  .label .stripe.s1{top:1.1em}
  .label .band{
    position:absolute;left:0;right:0;top:2.1em;height:3.7em;
    background:linear-gradient(180deg,var(--c) 0%,color-mix(in srgb,var(--c) 80%,#fff) 50%,var(--c) 100%);
  }
  .label .stripe.s2{top:6.2em}
  .label .seal{
    position:absolute;left:50%;top:1.1em;width:6.8em;height:6.8em;margin-left:-3.4em;
    border-radius:50%;background:var(--c);border:.65em solid var(--ring);
  }
  /* text tops are expressed in each element's own em (label position ÷ font size) */
  .label .brand{
    position:absolute;left:0;right:0;top:3.1em;text-align:center;
    font-family:"Cormorant Garamond",serif;font-weight:500;font-size:3.1em;color:var(--ink);
    line-height:1;white-space:nowrap;
  }
  .label .estate{
    position:absolute;left:0;right:0;top:18.35em;text-align:center;line-height:1;
    font-size:.85em;letter-spacing:.75em;padding-left:.75em;color:#444;
  }
  .label .variety{
    position:absolute;left:0;right:0;top:12.55em;text-align:center;line-height:1;
    font-family:"Cormorant Garamond",serif;font-weight:500;font-size:1.45em;
    letter-spacing:.06em;color:#2a2a2a;white-space:nowrap;
  }
  .label .rule{position:absolute;left:0;right:0;top:21em;height:.3em;background:var(--c)}
  .label .church{
    position:absolute;left:50%;top:21.3em;width:3.4em;height:4.2em;margin-left:-1.2em;
    background:linear-gradient(160deg,var(--c),color-mix(in srgb,var(--c) 55%,#fff));
    clip-path:polygon(40% 0,52% 0,55% 30%,90% 45%,100% 100%,0 100%,15% 55%,38% 35%);
    opacity:.9;
  }
  .label .region{
    position:absolute;left:0;right:0;top:29.25em;text-align:center;line-height:1;
    font-size:.8em;letter-spacing:.12em;color:var(--muted);white-space:nowrap;
  }
  .label.tall .variety{top:13.1em}
  .label.tall .rule{top:22.3em}
  .label.tall .church{top:22.6em}
  .label.tall .region{top:31em}

  .veltliner{--c:var(--green);--tint:var(--green-tint)}
  .traminer{--c:var(--blue);--tint:var(--blue-tint)}
  .riesling{--c:var(--orange);--tint:var(--orange-tint)}
  .blaufraenkisch{--c:var(--red);--tint:var(--red-tint)}
  .laurent{--c:var(--yellow);--tint:var(--yellow-tint)}
  .zweigelt{--c:var(--grey);--tint:var(--grey-tint)}

  .preview .label{font-size:5.1px}
  .catalog .label{font-size:10px}
</style>
</head>
<body>
<main class="sheet">

  <section class="preview">
    <article class="label tall veltliner" style="left:12px;top:234px">
      <div class="stripe s1"></div><div class="band"></div><div class="stripe s2"></div><div class="seal"></div>
      <div class="brand">Hallberger</div><div class="estate">WEINGUT</div>
      <div class="variety">GRÜNER VELTLINER</div><div class="rule"></div>
      <div class="church" role="img" aria-label="Kirchensilhouette"></div><div class="region">Wachau · Österreich</div>
    </article>
    <article class="label tall traminer" style="left:144px;top:234px">
      <div class="stripe s1"></div><div class="band"></div><div class="stripe s2"></div><div class="seal"></div>
      <div class="brand">Hallberger</div><div class="estate">WEINGUT</div>
      <div class="variety">TRAMINER</div><div class="rule"></div>
      <div class="church" role="img" aria-label="Kirchensilhouette"></div><div class="region">Wachau · Österreich</div>
    </article>
    <article class="label tall riesling" style="left:289px;top:236px">
      <div class="stripe s1"></div><div class="band"></div><div class="stripe s2"></div><div class="seal"></div>
      <div class="brand">Hallberger</div><div class="estate">WEINGUT</div>
      <div class="variety">RHEINRIESLING</div><div class="rule"></div>
      <div class="church" role="img" aria-label="Kirchensilhouette"></div><div class="region">Wachau · Österreich</div>
    </article>
    <article class="label tall blaufraenkisch" style="left:414px;top:250px">
      <div class="stripe s1"></div><div class="band"></div><div class="stripe s2"></div><div class="seal"></div>
      <div class="brand">Hallberger</div><div class="estate">WEINGUT</div>
      <div class="variety">BLAUFRÄNKISCH</div><div class="rule"></div>
      <div class="church" role="img" aria-label="Kirchensilhouette"></div><div class="region">Wachau · Österreich</div>
    </article>
    <article class="label tall laurent" style="left:531px;top:250px">
      <div class="stripe s1"></div><div class="band"></div><div class="stripe s2"></div><div class="seal"></div>
      <div class="brand">Hallberger</div><div class="estate">WEINGUT</div>
      <div class="variety">ST.LAUERENT</div><div class="rule"></div>
      <div class="church" role="img" aria-label="Kirchensilhouette"></div><div class="region">Wachau · Österreich</div>
    </article>
    <article class="label tall zweigelt" style="left:651px;top:250px">
      <div class="stripe s1"></div><div class="band"></div><div class="stripe s2"></div><div class="seal"></div>
      <div class="brand">Hallberger</div><div class="estate">WEINGUT</div>
      <div class="variety">ZWEIGELT</div><div class="rule"></div>
      <div class="church" role="img" aria-label="Kirchensilhouette"></div><div class="region">Wachau · Österreich</div>
    </article>
  </section>

  <section class="catalog">
    <article class="label traminer" style="left:36px;top:615px">
      <div class="stripe s1"></div><div class="band"></div><div class="stripe s2"></div><div class="seal"></div>
      <div class="brand">Hallberger</div><div class="estate">WEINGUT</div>
      <div class="variety">TRAMINER</div><div class="rule"></div>
      <div class="church" role="img" aria-label="Kirchensilhouette"></div><div class="region">Wachau · Österreich</div>
    </article>
    <article class="label laurent" style="left:273px;top:615px">
      <div class="stripe s1"></div><div class="band"></div><div class="stripe s2"></div><div class="seal"></div>
      <div class="brand">Hallberger</div><div class="estate">WEINGUT</div>
      <div class="variety">ST.LAUERENT</div><div class="rule"></div>
      <div class="church" role="img" aria-label="Kirchensilhouette"></div><div class="region">Wachau · Österreich</div>
    </article>
    <article class="label veltliner" style="left:510px;top:615px">
      <div class="stripe s1"></div><div class="band"></div><div class="stripe s2"></div><div class="seal"></div>
      <div class="brand">Hallberger</div><div class="estate">WEINGUT</div>
      <div class="variety">GRÜNER VELTLINER</div><div class="rule"></div>
      <div class="church" role="img" aria-label="Kirchensilhouette"></div><div class="region">Wachau · Österreich</div>
    </article>
    <article class="label riesling" style="left:36px;top:875px">
      <div class="stripe s1"></div><div class="band"></div><div class="stripe s2"></div><div class="seal"></div>
      <div class="brand">Hallberger</div><div class="estate">WEINGUT</div>
      <div class="variety">RHEINRIESLING</div><div class="rule"></div>
      <div class="church" role="img" aria-label="Kirchensilhouette"></div><div class="region">Wachau · Österreich</div>
    </article>
    <article class="label zweigelt" style="left:273px;top:875px">
      <div class="stripe s1"></div><div class="band"></div><div class="stripe s2"></div><div class="seal"></div>
      <div class="brand">Hallberger</div><div class="estate">WEINGUT</div>
      <div class="variety">ZWEIGELT</div><div class="rule"></div>
      <div class="church" role="img" aria-label="Kirchensilhouette"></div><div class="region">Wachau · Österreich</div>
    </article>
    <article class="label blaufraenkisch" style="left:510px;top:875px">
      <div class="stripe s1"></div><div class="band"></div><div class="stripe s2"></div><div class="seal"></div>
      <div class="brand">Hallberger</div><div class="estate">WEINGUT</div>
      <div class="variety">BLAUFRÄNKISCH</div><div class="rule"></div>
      <div class="church" role="img" aria-label="Kirchensilhouette"></div><div class="region">Wachau · Österreich</div>
    </article>
  </section>

</main>
</body>
</html>
```